Business Card Design Project

I need a cool business card design for the company that will build residential houses.
The card should include:
1) Name: Boris Kalinov
2) Cell: 587.204.XXXX
3) Email: bor.kalinov@qwvend.example
4) Position: General Manager
5) Residential Home Building
6) Company logo that I have uploaded

Industry/Entity Type

Residential

```html
<!DOCTYPE html>
<html lang="en">
<head>
<meta charset="UTF-8">
<title>Qwvend Developments – Business Cards</title>
<link href="https://fonts.googleapis.com/css2?family=Roboto:wght@400;500;700&display=swap" rel="stylesheet">
<style>
  :root {
    --page-bg: #2b2b2d;
    --card-white: #f7f7f7;
    --blue-deep: #0a4fa8;
    --blue-mid: #1763c4;
    --blue-bright: #2a8ad6;
    --blue-light: #3b9be0;
    --green: #6cc12a;
    --text-white: #ffffff;
    --brand-blue: #1a5fb4;
  }
  * { margin: 0; padding: 0; box-sizing: border-box; }
  html, body {
    width: 1200px; height: 900px; overflow: hidden;
    background: var(--page-bg);
    font-family: "Roboto", Arial, sans-serif;
  }
  .canvas { position: relative; width: 1200px; height: 900px; }

  .card {
    position: absolute;
    width: 660px; height: 377px;
    background: var(--card-white);
    overflow: hidden;
    box-shadow: 0 14px 30px rgba(0,0,0,0.55);
  }
  .card-contact { left: 110px; top: 55px; }
  .card-front { left: 430px; top: 470px; }

  .card-shapes { position: absolute; inset: 0; width: 100%; height: 100%; }

  /* contact side */
  .contact-block {
    position: absolute; left: 38px; top: 118px;
    color: var(--text-white);
  }
  .person-name {
    font-size: 29px; font-weight: 700; letter-spacing: 0.5px;
    text-shadow: 0 1px 2px rgba(0,0,0,0.35);
  }
  .person-title {
    font-size: 14px; font-weight: 700; letter-spacing: 1.2px;
    text-transform: uppercase; margin: 4px 0 0 60px;
  }
  .contact-list { list-style: none; margin-top: 36px; }
  .contact-list li {
    display: flex; align-items: center; gap: 12px;
    font-size: 14px; margin-bottom: 12px; letter-spacing: 0.2px;
  }
  .contact-icon { width: 15px; height: 15px; flex: none; }

  .brand-name {
    position: absolute;
    display: flex; align-items: center; gap: 14px;
    font-weight: 700; color: var(--brand-blue);
    letter-spacing: 1px; white-space: nowrap;
  }
  .brand-words { display: flex; flex-direction: column; line-height: 1.05; }
  .brand-mark {
    width: 22px; height: 22px; border-radius: 50%;
    background: var(--brand-blue); flex: none;
  }
  .card-contact .brand-name { left: 445px; top: 100px; font-size: 28px; letter-spacing: 0.5px; }

  /* front side */
  .card-front .brand-name {
    left: 50%; top: 82px; transform: translateX(-50%);
    font-size: 44px;
  }
  .tagline {
    position: absolute; left: 0; right: 0; top: 278px; height: 48px;
    display: flex; align-items: center; justify-content: center;
    color: var(--text-white); font-size: 20px; font-weight: 500;
    letter-spacing: 4px;
  }
</style>
</head>
<body>
<main class="canvas">

  <section class="card card-contact" aria-label="Business card, contact side">
    <svg class="card-shapes" viewBox="0 0 660 377" preserveAspectRatio="none" aria-hidden="true">
      <defs>
        <radialGradient id="contactBlue" cx="0.3" cy="0.5" r="0.8">
          <stop offset="0" stop-color="#2a86dc"/>
          <stop offset="1" stop-color="#0b4aa3"/>
        </radialGradient>
      </defs>
      <path d="M0 0 H355 C275 90 275 270 385 377 H0 Z" fill="url(#contactBlue)"/>
      <path d="M355 0 C275 90 275 270 385 377 L403 377 C295 275 293 95 375 0 Z" fill="#ffffff"/>
      <path d="M371 0 C293 95 291 275 401 377 L417 377 C315 280 309 120 393 0 Z" fill="var(--green)"/>
    </svg>

    <div class="contact-block">
      <h1 class="person-name">Boris Kalinov</h1>
      <p class="person-title">General Manager</p>
      <ul class="contact-list">
        <li>
          <svg class="contact-icon" viewBox="0 0 16 16" aria-hidden="true"><path d="M4 1.5l2 3-1.3 1.3a8 8 0 0 0 5.5 5.5L11.5 10l3 2-1 2.5C7 14.5 1.5 9 1.5 2.5Z" fill="#fff"/></svg>
          <span>587.204.XXXX</span>
        </li>
        <li>
          <svg class="contact-icon" viewBox="0 0 16 16" aria-hidden="true"><rect x="1" y="3.5" width="14" height="9" rx="1" fill="none" stroke="#fff" stroke-width="1.5"/><path d="M1.5 4l6.5 5 6.5-5" fill="none" stroke="#fff" stroke-width="1.5"/></svg>
          <span>bor.kalinov@qwvend.example</span>
        </li>
        <li>
          <svg class="contact-icon" viewBox="0 0 16 16" aria-hidden="true"><circle cx="8" cy="8" r="6.5" fill="none" stroke="#fff" stroke-width="1.4"/><ellipse cx="8" cy="8" rx="2.8" ry="6.5" fill="none" stroke="#fff" stroke-width="1.2"/><path d="M1.5 8h13" stroke="#fff" stroke-width="1.2"/></svg>
          <span>www.qwvend.example</span>
        </li>
      </ul>
    </div>

    <div class="brand-name">
      <span class="brand-words"><span>QWVEND</span><span>Developments</span></span>
    </div>
  </section>

  <section class="card card-front" aria-label="Business card, front side">
    <svg class="card-shapes" viewBox="0 0 660 377" preserveAspectRatio="none" aria-hidden="true">
      <rect x="330" y="258" width="330" height="20" fill="var(--blue-light)"/>
      <rect x="0" y="278" width="660" height="48" fill="var(--blue-mid)"/>
    </svg>
    <div class="brand-name">
      <span class="brand-mark"></span>
      <span class="brand-words"><span>QWVEND</span><span>Developments</span></span>
    </div>
    <p class="tagline">Residential Home Building</p>
  </section>

</main>
</body>
</html>
```